Flyer Design / Authenticity Certificate - Art Work

Looking for a design of a "Authenticity Certificate" - flyer, that will include some basic company info like logo etc, and allow our in house artist to sign and authenticate before it is applied the reverse of one of the paintings we will sell. Linked with our online sales website - "Amber Harbor Studios", where we recreate one off oil paintings from digital photographs. Our business logo should be incorporated in the design, along with a section for "Artisit Name" "Artisit Signature" "Ref Code"
Updates

Hi.. Sorry I should have added the size we need - please design accordingly to A6. Thanks.

Industry/Entity Type

It Company

Font styles to use
Serif
Script

Colors

Designer to choose colors to be used in the design.

Requirements
Must have
• Company logo
• Area for artist to print and sign
• Area for a reference
Nice to have
• must use the logo, maybe incorporate a "seal" icon, like what was used as a wax seal on older style documents

```html
<!DOCTYPE html>
<html lang="en">
<head>
<meta charset="utf-8">
<title>Authenticity Certificate – Amber Harbor Studios</title>
<link rel="stylesheet" href="https://fonts.googleapis.com/css2?family=Exo+2:wght@300;600&family=Ubuntu:ital,wght@0,400;0,500;1,400&family=Great+Vibes&display=swap">
<style>
  :root {
    --backdrop: #9464a3;
    --paper: #f4f2ef;
    --paper-shade: #e9e6e1;
    --ink: #3a3a3c;
    --gold: #c3962f;
    --gold-light: #dcbf78;
    --rule: #2f2f31;
  }
  * { margin: 0; padding: 0; box-sizing: border-box; }
  html, body { width: 1148px; height: 1200px; overflow: hidden; }
  body { background: var(--backdrop); position: relative; }

  .certificate {
    position: absolute; left: 176px; top: 40px;
    width: 796px; height: 1120px;
    background: var(--paper);
    overflow: hidden;
  }
  .certificate__pattern {
    position: absolute; inset: 0;
    background: radial-gradient(circle at 50% 45%, var(--paper) 0%, var(--paper-shade) 100%);
  }
  .ornament { position: absolute; width: 297px; height: 379px; }
  .ornament--tl { left: 39px; top: 42px; }
  .ornament--tr { right: 39px; top: 42px; transform: scaleX(-1); }
  .ornament--bl { left: 39px; top: 695px; transform: scaleY(-1); }
  .ornament--br { right: 39px; top: 695px; transform: scale(-1,-1); }

  .brand { position: absolute; left: 0; right: 0; top: 116px; text-align: center; }
  .brand__mark {
    width: 134px; height: 134px; margin: 0 auto;
    border-radius: 50%; background: var(--ink);
  }
  .brand__name {
    margin-top: 18px;
    font: 600 28px/1 "Exo 2", sans-serif; letter-spacing: 2px;
    color: var(--ink);
  }

  .title {
    position: absolute; left: 0; right: 0; top: 356px; text-align: center;
    font: 600 66px/1 "Exo 2", sans-serif; color: var(--ink);
  }
  .subtitle {
    position: absolute; left: 0; right: 0; top: 430px; text-align: center;
    font: 300 36px/1 "Exo 2", sans-serif; color: var(--ink);
  }
  .presented {
    position: absolute; left: 0; right: 0; top: 497px; text-align: center;
    font: italic 400 29px/1 "Ubuntu", sans-serif; color: var(--ink);
  }
  .recipient {
    position: absolute; left: 0; right: 0; top: 535px; text-align: center;
    font: 400 92px/1.1 "Great Vibes", cursive; color: var(--gold);
  }
  .statement {
    position: absolute; left: 120px; width: 556px; top: 675px;
    font: 400 13.6px/1.47 "Ubuntu", sans-serif; color: var(--ink);
    text-align: justify;
  }

  .reference {
    position: absolute; left: 0; right: 0; top: 770px;
    display: flex; justify-content: center; align-items: flex-end; gap: 8px;
    font: 500 14px/1 "Ubuntu", sans-serif; color: var(--ink);
  }
  .reference__field { width: 130px; border-bottom: 2px solid var(--rule); height: 14px; }

  .signature { position: absolute; top: 813px; width: 144px; text-align: center; }
  .signature--left { left: 147px; }
  .signature--right { left: 498px; }
  .signature__line { border-top: 2px solid var(--rule); }
  .signature__label {
    margin-top: 6px; font: 500 14px/1 "Ubuntu", sans-serif; color: var(--ink);
  }

  .seal { position: absolute; left: 338px; top: 848px; width: 112px; height: 170px; }
</style>
</head>
<body>
  <main class="certificate">
    <div class="certificate__pattern" role="img" aria-label="Faint decorative floral paisley pattern across the paper"></div>

    <svg class="ornament ornament--tl" viewBox="0 0 297 379" role="img" aria-label="Gold baroque corner flourish">
      <path d="M0 379 L0 0 L297 0 L297 40 L60 40 Q40 40 40 60 L40 379 Z" fill="var(--gold-light)" opacity="0.75"/>
    </svg>
    <svg class="ornament ornament--tr" viewBox="0 0 297 379" role="img" aria-label="Gold baroque corner flourish">
      <path d="M0 379 L0 0 L297 0 L297 40 L60 40 Q40 40 40 60 L40 379 Z" fill="var(--gold-light)" opacity="0.75"/>
    </svg>
    <svg class="ornament ornament--bl" viewBox="0 0 297 379" role="img" aria-label="Gold baroque corner flourish">
      <path d="M0 379 L0 0 L297 0 L297 40 L60 40 Q40 40 40 60 L40 379 Z" fill="var(--gold-light)" opacity="0.75"/>
    </svg>
    <svg class="ornament ornament--br" viewBox="0 0 297 379" role="img" aria-label="Gold baroque corner flourish">
      <path d="M0 379 L0 0 L297 0 L297 40 L60 40 Q40 40 40 60 L40 379 Z" fill="var(--gold-light)" opacity="0.75"/>
    </svg>

    <header class="brand">
      <div class="brand__mark"></div>
      <p class="brand__name">AMBER HARBOR STUDIOS</p>
    </header>

    <h1 class="title">AUTHENTICITY</h1>
    <p class="subtitle">Certificate</p>
    <p class="presented">This Certificate Is Presented To</p>
    <p class="recipient">Johnathan Doe</p>

    <p class="statement">This certifies that the accompanying one-off oil painting was recreated by hand from the owner's digital photograph by an Amber Harbor Studios artist. Each piece is painted with care, inspected before shipping and recorded under the reference code below. Please keep this certificate with the artwork as proof of its origin and authenticity.</p>

    <div class="reference">
      <span class="reference__label">Ref Code:</span>
      <span class="reference__field"></span>
    </div>

    <div class="signature signature--left">
      <div class="signature__line"></div>
      <p class="signature__label">Artist Name</p>
    </div>
    <div class="signature signature--right">
      <div class="signature__line"></div>
      <p class="signature__label">Artist Signature</p>
    </div>

    <svg class="seal" viewBox="0 0 112 170" aria-hidden="true">
      <path d="M30 80 L14 160 L32 148 L42 168 L56 92 Z" fill="var(--gold)"/>
      <path d="M82 80 L98 160 L80 148 L70 168 L56 92 Z" fill="var(--gold)"/>
      <circle cx="56" cy="56" r="54" fill="var(--gold)"/>
      <circle cx="56" cy="56" r="40" fill="var(--ink)"/>
    </svg>
  </main>
</body>
</html>
```